Gift Card/voucher Design for Beauty Clinic

I need a design for a gift card I Can use in all seasons for my Aesthetic clinic. The Logo is attached. The main colors we use are white and black, we are open for new suggestions to make an friendly yet professional impression. Ideally the gift card/voucher would be foldable.
The inside should contain the following fields:

Für:

Von:

Wert

Gültigkeit

```html
<!DOCTYPE html>
<html lang="de">
<head>
<meta charset="utf-8">
<title>Helena Marwick Aesthetics – Gift Card</title>
<link rel="stylesheet" href="https://fonts.googleapis.com/css2?family=Playfair+Display:wght@400;700&family=Montserrat:wght@400&display=swap">
<style>
  :root {
    --page-bg: #ebe7e1;
    --navy: #172734;
    --white: #ffffff;
    --ink: #1b2530;
    --card-light: #f2f2f1;
    --petal: #f7f7f5;
    --leaf: #5f8f4a;
    --leaf-dark: #3f6b32;
    --field: rgba(255, 255, 255, 0.9);
  }
  * { margin: 0; padding: 0; box-sizing: border-box; }
  html, body {
    width: 900px;
    height: 1200px;
    overflow: hidden;
    background: var(--page-bg);
  }
  .canvas {
    position: relative;
    width: 900px;
    height: 1200px;
  }
  .card {
    position: absolute;
    width: 773px;
    height: 448px;
    border-radius: 22px;
    overflow: hidden;
    box-shadow: 0 6px 18px rgba(0, 0, 0, 0.18);
  }
  .card--front { left: 72px; top: 135px; background: var(--navy); }
  .card--back { left: 74px; top: 625px; background: var(--card-light); }

  .card__art { position: absolute; inset: 0; width: 100%; height: 100%; }

  .brand {
    position: absolute;
    left: 28px;
    width: 492px;
    top: 0;
    height: 100%;
    text-align: center;
    color: var(--white);
  }
  .brand__mark {
    position: absolute;
    left: 50%;
    top: 110px;
    width: 120px;
    height: 120px;
    margin-left: -60px;
    border: 2px solid var(--white);
    border-radius: 50%;
  }
  .brand__name {
    position: absolute;
    left: 0; right: 0;
    top: 292px;
    font-family: "Playfair Display", serif;
    font-weight: 400;
    font-size: 31px;
    letter-spacing: 1.5px;
  }
  .brand__tagline {
    position: absolute;
    left: 0; right: 0;
    top: 339px;
    font-family: "Montserrat", sans-serif;
    font-size: 17px;
    letter-spacing: 7px;
  }
  .gift-label {
    position: absolute;
    left: 714px;
    top: 227px;
    transform: translate(-50%, -50%) rotate(-90deg);
    font-family: "Playfair Display", serif;
    font-weight: 700;
    font-size: 26px;
    letter-spacing: 1px;
    color: var(--ink);
    white-space: nowrap;
  }

  .back-photo {
    position: absolute;
    inset: 0;
    background:
      radial-gradient(ellipse 260px 220px at 720px 220px, rgba(255,255,255,0.95), rgba(255,255,255,0) 70%),
      radial-gradient(ellipse 420px 150px at 420px 400px, rgba(255,255,255,0.9), rgba(255,255,255,0) 75%),
      linear-gradient(200deg, rgba(242,242,241,1) 25%, rgba(200,214,190,0.9) 60%, rgba(110,150,90,0.75) 100%);
  }
  .fields {
    position: absolute;
    left: 97px;
    top: 103px;
    width: 578px;
    list-style: none;
  }
  .field {
    height: 40px;
    margin-bottom: 28px;
    border-radius: 20px;
    background: var(--field);
    box-shadow: 0 2px 6px rgba(0, 0, 0, 0.08);
    padding-left: 27px;
    font-family: "Playfair Display", serif;
    font-size: 24px;
    line-height: 40px;
    color: var(--ink);
  }
</style>
</head>
<body>
<main class="canvas">

  <section class="card card--front" aria-label="Gift card front">
    <svg class="card__art" viewBox="0 0 773 448" xmlns="http://www.w3.org/2000/svg">
      <defs>
        <linearGradient id="tulipTones" x1="0" y1="0" x2="0.3" y2="1">
          <stop offset="0" stop-color="#f1f1ef"/>
          <stop offset="0.45" stop-color="#e9ece6"/>
          <stop offset="0.75" stop-color="#8fb07a"/>
          <stop offset="1" stop-color="#4f7f3e"/>
        </linearGradient>
        <clipPath id="photoArea"><polygon points="588,0 773,0 773,448 398,448"/></clipPath>
        <clipPath id="navyArea"><polygon points="0,0 588,0 398,448 0,448"/></clipPath>
      </defs>
      <polygon points="588,0 773,0 773,448 398,448" fill="url(#tulipTones)" role="img" aria-label="Photo of white tulips with green leaves"/>
      <rect x="28" y="33" width="715" height="385" fill="none" stroke="#ffffff" stroke-width="2" clip-path="url(#navyArea)"/>
      <rect x="28" y="33" width="715" height="385" fill="none" stroke="#172734" stroke-width="2" clip-path="url(#photoArea)"/>
      <line x1="714" y1="48" x2="714" y2="135" stroke="#172734" stroke-width="2"/>
      <line x1="714" y1="322" x2="714" y2="405" stroke="#172734" stroke-width="2"/>
    </svg>
    <div class="brand">
      <span class="brand__mark" aria-hidden="true"></span>
      <p class="brand__name">HELENA MARWICK</p>
      <p class="brand__tagline">AESTHETICS</p>
    </div>
    <p class="gift-label">GIFT CARD</p>
  </section>

  <section class="card card--back" aria-label="Gift card back">
    <div class="back-photo" role="img" aria-label="Soft photo of white tulips with green leaves"></div>
    <ul class="fields">
      <li class="field">Für:</li>
      <li class="field">Von:</li>
      <li class="field">Wert</li>
      <li class="field">Gültigkeit</li>
    </ul>
  </section>

</main>
</body>
</html>
```